Design a double sided business card

We are looking for a clean, eye-catching, and contemporary design that enhances the brand and presents a premium, professional image. Our preference is for a brown card with black gloss detailing and embossed elements; however, we are open to creative input and design suggestions that best achieve a strong visual impact.

Please see the attached existing business card for reference. We use both black and brown colours consistently across our branding.

On sample provided

```html
<!DOCTYPE html>
<html lang="en">
<head>
<meta charset="utf-8">
<title>Korvan business card</title>
<link href="https://fonts.googleapis.com/css2?family=Montserrat:wght@400;500;700;800&display=swap" rel="stylesheet">
<style>
  :root {
    --backdrop: #2b2b2b;
    --card: #c8b59b;
    --ink: #141414;
    --card-radius: 20px;
  }
  * { box-sizing: border-box; margin: 0; padding: 0; }
  html, body { width: 1200px; height: 900px; overflow: hidden; }
  body {
    background: var(--backdrop);
    font-family: "Montserrat", sans-serif;
    color: var(--ink);
    position: relative;
  }
  .card {
    position: absolute;
    width: 525px;
    height: 300px;
    background: var(--card);
    border-radius: var(--card-radius);
  }
  .card--front { left: 70px; top: 80px; }
  .card--back { left: 605px; top: 500px; }

  .brand {
    display: flex;
    align-items: center;
    justify-content: center;
    gap: 12px;
  }
  .brand__square {
    width: 30px; height: 30px;
    background: var(--ink);
  }
  .brand__name {
    font-weight: 800;
    letter-spacing: 0.08em;
    font-size: 44px;
    line-height: 1;
  }

  .card--front .brand { position: absolute; left: 0; right: 0; top: 105px; }
  .front__url {
    position: absolute; left: 0; right: 0; top: 232px;
    text-align: center;
    font-size: 12px;
    letter-spacing: 0.28em;
    font-weight: 500;
  }

  .card--back .brand { position: absolute; left: 0; right: 0; top: 42px; }
  .card--back .brand__name { font-size: 34px; }
  .card--back .brand__square { width: 24px; height: 24px; }
  .holder {
    position: absolute; left: 0; right: 0; top: 98px;
    text-align: center;
  }
  .holder__name { font-weight: 800; font-size: 17px; letter-spacing: 0.02em; }
  .holder__role { font-size: 11px; font-weight: 500; margin-top: 1px; }

  .rule { position: absolute; height: 1px; background: var(--ink); }
  .rule--contact { left: 28px; width: 230px; top: 196px; }
  .rule--address { right: 28px; width: 200px; top: 196px; }

  .contact-list {
    position: absolute; left: 32px; top: 208px;
    list-style: none;
    font-size: 12.5px;
  }
  .address {
    position: absolute; right: 30px; top: 208px;
    list-style: none;
    font-size: 12.5px;
    text-align: right;
  }
  .contact-list li, .address li {
    display: flex; align-items: center; gap: 8px;
    height: 22px;
  }
  .address li { justify-content: flex-end; }
  .icon { width: 12px; height: 12px; fill: none; stroke: var(--ink); stroke-width: 1.6; }
</style>
</head>
<body>
  <section class="card card--front" aria-label="Card front">
    <div class="brand">
      <span class="brand__square"></span>
      <span class="brand__name">KORVAN</span>
    </div>
    <p class="front__url">WWW.KORVAN.CO.UK</p>
  </section>

  <section class="card card--back" aria-label="Card back">
    <div class="brand">
      <span class="brand__square"></span>
      <span class="brand__name">KORVAN</span>
    </div>
    <div class="holder">
      <p class="holder__name">LEO MARSH</p>
      <p class="holder__role">Director</p>
    </div>

    <div class="rule rule--contact"></div>
    <ul class="contact-list">
      <li>
        <svg class="icon" viewBox="0 0 12 12"><path d="M2 1.5l2 .2 1 2.3-1.2 1a6 6 0 0 0 3.2 3.2l1-1.2 2.3 1 .2 2c-5 .6-9-3.5-8.5-8.5z"/></svg>
        0800 555 0142
      </li>
      <li>
        <svg class="icon" viewBox="0 0 12 12"><rect x="3" y="1" width="6" height="10" rx="1"/><path d="M5.5 9.2h1"/></svg>
        07700900418
      </li>
      <li>
        <svg class="icon" viewBox="0 0 12 12"><rect x="1" y="2.5" width="10" height="7"/><path d="M1 2.5l5 4 5-4"/></svg>
        leo@korvan.co.uk
      </li>
    </ul>

    <div class="rule rule--address"></div>
    <ul class="address">
      <li>12 Orchard Mews Lane</li>
      <li>Northfield AB1 2CD</li>
      <li>
        <svg class="icon" viewBox="0 0 12 12"><circle cx="6" cy="6" r="5"/><path d="M1 6h10M6 1c-2.5 3-2.5 7 0 10M6 1c2.5 3 2.5 7 0 10"/></svg>
        www.korvan.co.uk
      </li>
    </ul>
  </section>
</body>
</html>
```